Manufacturing business needs a website revamp

We are a manufacturing business supplying parts and modules to mid-high end consumer electronics brands from kitchen appliances to powered tools mainly in US/Europe. We want design ideas for a revamp of our website. We're aiming for a look and feel that's sleek, tidy and modern whilst still providing the right balance for content. A smooth and comfortable user experience that directs users to the information they may be looking for and promote our services. Something that incorporates design ideas such as: responsive design, lazy loading, slider banners, responsive layout, dynamic scrolling, liquid layout, full page headers etc... These are just terms bounced around within our team and certainly neither exclusive nor absolutely necessary. This is our current website for reference: https://www.varlumotek.com/ , which we feel is both outdated and doesn't engage visitors.

Attached is our planned new site map (we’re open to additional ideas here). We would like mock ups for each page on the site map. We will subsequently fill out the contents ourselves, but require design directions on e.g. how much text should go at which spot. E.g. for our Automotive page under Industries, we would like a suitable layout to be designed, as well as designated areas for texts. As for assets, please use any of the assets already on our current site or external source. We’ve yet to finalize on our selection of assets so please use the above as placeholders for now. Additionally, we would want a mock up for a pop-up frame to showcase additional technical specifications for some of our product ranges. For example, under the powertools section of our current website, we have additional listings under our product range. Currently they do not have a pop up function, but if we were to create a pop up frame to display detailed specifications, what layout should we use?

Finally, our target audiences are professional representatives from leading consumer brands who may be interested in our services. Our target customers are mid-high end brands. Think, for example, KVR/Harwick for automotive, Frostivane/Trell/Dovarin for consumer electronics/kitchen appliances, and Pelham Grove & Tasker/Brantover for powered tools. Typically it will be their product designers/engineers and supply chain representatives who will visit our website.

Target Market(s)

Professional product engineers/designers from mid-high end consumer electronics brands.

Industry/Entity Type

Manufacturing

Contact Information for Business Card

Attached are back and front of our current name card design. Again, we're open to changes that matches the style of our future website design. A few notes on the business card design:
- Cannot have blue background
- Does not have to be bilingual. I.e. open to single language design on one side and logo on the other

Coding

Coded - Design and coding required

Number of Pages Required

5+ page

Font styles to use
Sans Serif

Colors
3176b5

Requirements
Must have
• Color scheme must be based on the blue from our current website design. We will be keeping our current logo, hence must match that logo.
Nice to have
• Plim (or similar platforms) as demos/final solutions ok.
Should not have
• See brief

```html
<!DOCTYPE html>
<html lang="en">
<head>
<meta charset="utf-8">
<title>Varlumo — Manufacturing</title>
<link href="https://fonts.googleapis.com/css2?family=Poppins:wght@400;500;600;700;800&family=Open+Sans:wght@400;600&display=swap" rel="stylesheet">
<style>
:root{
  --blue:#3176b5;
  --blue-dark:#245d93;
  --navy:#17263a;
  --navy-2:#1f3047;
  --ink:#2b2f36;
  --muted:#6b7380;
  --line:#d9dee5;
  --light:#f3f5f8;
  --white:#ffffff;
}
*{margin:0;padding:0;box-sizing:border-box}
html,body{width:1200px;height:3208px;overflow:hidden}
body{font-family:"Open Sans",Arial,sans-serif;color:var(--ink);background:var(--white);position:relative}
h1,h2,h3,h4,.brand,.nav a,.btn{font-family:"Poppins",Arial,sans-serif}

/* Hero */
.hero{position:absolute;left:0;top:0;width:1200px;height:640px;overflow:hidden}
.hero-photo{position:absolute;inset:0;background:linear-gradient(90deg,#151d27 0%,#1d2630 40%,#3a3d3c 62%,#6a5b46 78%,#3b3a36 100%)}
.hero-shade{position:absolute;inset:0;background:linear-gradient(90deg,rgba(10,15,22,.75) 0%,rgba(10,15,22,.35) 55%,rgba(10,15,22,0) 100%)}
.topbar{position:absolute;left:0;top:0;width:100%;height:34px;background:rgba(8,12,18,.7);display:flex;align-items:center;justify-content:space-between;padding:0 60px;font-size:12px;color:#d8dde4}
.topbar .links span{margin-right:14px}
.lang{border:1px solid rgba(255,255,255,.35);padding:2px 10px;font-size:11px}
.nav{position:absolute;left:0;top:50px;width:100%;display:flex;align-items:center;justify-content:space-between;padding:0 60px}
.brand{display:flex;align-items:center;gap:10px;font-weight:700;font-size:26px;color:var(--white)}
.brand .mark{width:22px;height:22px;background:var(--blue)}
.nav ul{list-style:none;display:flex;gap:30px}
.nav a{color:var(--white);text-decoration:none;font-size:13px;font-weight:500}
.hero-copy{position:absolute;left:60px;top:355px;color:var(--white)}
.hero-copy h1{font-size:64px;font-weight:800;letter-spacing:1px;line-height:1}
.hero-copy h2{font-size:22px;font-weight:600;margin-top:10px}
.hero-copy p{font-size:15px;line-height:1.6;margin-top:22px;width:440px;color:#dfe4ea}
.btn{display:inline-block;margin-top:34px;background:var(--blue);color:var(--white);font-size:13px;font-weight:600;padding:13px 28px;letter-spacing:.5px}

/* Vision / Mission */
.vm{position:absolute;top:704px;left:60px;width:1080px;height:210px;display:flex;gap:30px}
.vm-card{flex:1;padding:40px 40px;position:relative}
.vm-card.vision{background:var(--white);border:1px solid var(--line);border-bottom:4px solid var(--blue)}
.vm-card.mission{background:var(--blue);color:var(--white)}
.vm-card h3{font-size:30px;font-weight:700;color:var(--blue)}
.vm-card.mission h3{color:var(--white)}
.vm-card p{font-size:13px;line-height:1.6;margin-top:14px;width:250px;color:var(--muted)}
.vm-card.mission p{color:#e3edf7;width:270px}
.vm-card svg{position:absolute;right:50px;top:55px}

/* Founded */
.founded{position:absolute;top:960px;left:0;width:1200px;text-align:center}
.founded h2{font-size:40px;font-weight:700;color:var(--blue)}
.founded p{font-size:14px;line-height:1.75;color:var(--muted);width:760px;margin:24px auto 0}
.founded p + p{margin-top:16px}

/* Industries */
.industries-band{position:absolute;top:1220px;left:0;width:1200px;height:270px;background:linear-gradient(120deg,#0f2a4a 0%,#1b3f6a 55%,#123052 100%)}
.industries h2{position:absolute;top:1260px;width:1200px;text-align:center;font-size:34px;font-weight:700;color:var(--white);letter-spacing:1px}
.ind-grid{position:absolute;top:1340px;left:98px;width:1004px;display:flex;gap:24px}
.ind-card{width:233px}
.ind-img{height:162px;border:4px solid var(--white)}
.ind-card h4{font-size:17px;font-weight:600;margin-top:22px;color:var(--ink)}
.ind-card p{font-size:12px;line-height:1.6;color:var(--muted);margin-top:8px;width:200px}

/* Core competencies */
.core-photo{position:absolute;top:1700px;left:0;width:600px;height:480px;background:linear-gradient(135deg,#1c2430 0%,#3a4350 45%,#8a6a3e 70%,#2a2f38 100%)}
.core-tag{position:absolute;top:2100px;left:300px;width:300px;height:80px;background:var(--blue);color:var(--white);font-family:"Poppins",Arial,sans-serif;font-size:16px;font-weight:600;display:flex;align-items:center;justify-content:center}
.core-text{position:absolute;top:1860px;left:700px;width:420px}
.core-text h2{font-size:34px;font-weight:700;color:var(--blue)}
.core-text p{font-size:14px;line-height:1.6;color:var(--muted);margin-top:12px;width:380px}
.core-list{list-style:none;margin-top:28px}
.core-list li{display:flex;align-items:center;gap:16px;font-size:14px;color:var(--ink);height:40px}

/* News */
.news h2{position:absolute;top:2262px;width:1200px;text-align:center;font-size:36px;font-weight:700;color:var(--blue)}
.news-grid{position:absolute;top:2345px;left:120px;width:960px;display:flex;gap:30px}
.news-card{width:300px;background:var(--white);box-shadow:0 4px 14px rgba(20,30,45,.1)}
.news-img{height:210px;position:relative}
.news-date{position:absolute;left:0;bottom:0;background:var(--blue);color:var(--white);font-size:11px;font-weight:600;padding:6px 16px}
.news-card p{font-size:12px;line-height:1.55;color:var(--ink);padding:18px 20px 24px;width:230px}

/* Footer */
.footer{position:absolute;top:2720px;left:0;width:1200px;height:488px;background:var(--navy);color:#c3cad4}
.f-cols{position:absolute;top:56px;left:60px;width:1080px;display:flex;gap:40px}
.f-col{flex:1;font-size:12px;line-height:1.8}
.f-col h4{font-size:15px;font-weight:600;color:var(--white);margin-bottom:34px}
.f-col p + p{margin-top:18px}
.f-bottom{position:absolute;left:60px;right:60px;bottom:0;height:120px;border-top:1px solid rgba(255,255,255,.12);font-size:11px;color:#98a3b1;padding-top:34px}
.f-bottom .brand{position:absolute;right:0;top:40px;font-size:24px}
</style>
</head>
<body>

<header class="hero">
  <div class="hero-photo" role="img" aria-label="Engineer in a hard hat and safety glasses working on a factory floor"></div>
  <div class="hero-shade"></div>
  <div class="topbar">
    <div class="links"><span>Careers</span>|&nbsp;&nbsp;<span>Quality Policy</span></div>
    <div class="lang">Language ▾</div>
  </div>
  <nav class="nav">
    <div class="brand"><span class="mark"></span>Varlumo</div>
    <ul>
      <li><a href="#">About Us</a></li>
      <li><a href="#">Industries</a></li>
      <li><a href="#">Core Competencies</a></li>
      <li><a href="#">News</a></li>
      <li><a href="#">Locations &amp; Contacts</a></li>
    </ul>
  </nav>
  <div class="hero-copy">
    <h1>MANUFACTURING</h1>
    <h2>We Supply Switches, Electronic Modules and Sensors</h2>
    <p>We deliver quality products at the fastest speed to market through our facilities in Asia and Europe</p>
    <span class="btn">VIEW MORE</span>
  </div>
</header>

<section class="vm">
  <div class="vm-card vision">
    <h3>VISION</h3>
    <p>Powering you up for success</p>
    <svg width="70" height="80" viewBox="0 0 70 80" fill="none" stroke="#b9c1cc" stroke-width="2"><rect x="8" y="6" width="44" height="60"/><line x1="16" y1="20" x2="44" y2="20"/><line x1="16" y1="30" x2="44" y2="30"/><line x1="16" y1="40" x2="36" y2="40"/><circle cx="52" cy="60" r="10"/></svg>
  </div>
  <div class="vm-card mission">
    <h3>MISSION</h3>
    <p>To exceed customers' expectations with the best innovative technologies, the best cost-effectiveness, and the utmost professional services</p>
    <svg width="80" height="80" viewBox="0 0 80 80" fill="none" stroke="rgba(255,255,255,.55)" stroke-width="2"><circle cx="36" cy="44" r="28"/><circle cx="36" cy="44" r="17"/><circle cx="36" cy="44" r="6"/><line x1="36" y1="44" x2="70" y2="10"/><polyline points="60,10 70,10 70,20"/></svg>
  </div>
</section>

<section class="founded">
  <h2>FOUNDED IN 1978</h2>
  <p>Our parent company was founded in 1978 as a switch manufacturer in Hong Kong. The Varlumo brand has achieved global recognition in various sectors.</p>
  <p>Over four decades later, we continue to facilitate our customers' innovation and production across the world with a wide range of integration solutions, enabling our customers to keep ahead of the competition.</p>
</section>

<section class="industries">
  <div class="industries-band" role="img" aria-label="Dark blue technology backdrop with circuit glow"></div>
  <h2>INDUSTRIES</h2>
  <div class="ind-grid">
    <div class="ind-card">
      <div class="ind-img" role="img" aria-label="Car dashboard controls" style="background:linear-gradient(135deg,#1f2a36,#4a5766)"></div>
      <h4>Automotive</h4>
      <p>Our commitment to your success is our drive to continuous</p>
    </div>
    <div class="ind-card">
      <div class="ind-img" role="img" aria-label="Home appliances lineup" style="background:linear-gradient(135deg,#2f8a8a,#bfc8cf)"></div>
      <h4>Electrical &amp; Electronic</h4>
      <p>Our commitment to your success is our drive to continuous</p>
    </div>
    <div class="ind-card">
      <div class="ind-img" role="img" aria-label="Cordless power tools" style="background:linear-gradient(135deg,#2a3542,#7a8591)"></div>
      <h4>Power Tools</h4>
      <p>Our commitment to your success is our drive to continuous</p>
    </div>
    <div class="ind-card">
      <div class="ind-img" role="img" aria-label="Sensor components in a laboratory" style="background:linear-gradient(135deg,#c9b89a,#e7e2d8)"></div>
      <h4>Sensors</h4>
      <p>Our commitment to your success is our drive to continuous</p>
    </div>
  </div>
</section>

<section class="core">
  <div class="core-photo" role="img" aria-label="Technician welding in a workshop"></div>
  <div class="core-tag">Research &amp; Development</div>
  <div class="core-text">
    <h2>CORE COMPETENCIES</h2>
    <p>Our commitment to your success is our drive to continuous innovation and improvement</p>
    <ul class="core-list">
      <li><svg width="20" height="20" viewBox="0 0 20 20"><circle cx="10" cy="10" r="9" fill="none" stroke="#3176b5" stroke-width="1.5"/><polyline points="8,6 12,10 8,14" fill="none" stroke="#3176b5" stroke-width="1.5"/></svg>Research &amp; Development</li>
      <li><svg width="20" height="20" viewBox="0 0 20 20"><circle cx="10" cy="10" r="9" fill="none" stroke="#3176b5" stroke-width="1.5"/><polyline points="8,6 12,10 8,14" fill="none" stroke="#3176b5" stroke-width="1.5"/></svg>Manufacturing Capabilities</li>
      <li><svg width="20" height="20" viewBox="0 0 20 20"><circle cx="10" cy="10" r="9" fill="none" stroke="#3176b5" stroke-width="1.5"/><polyline points="8,6 12,10 8,14" fill="none" stroke="#3176b5" stroke-width="1.5"/></svg>Process Management</li>
      <li><svg width="20" height="20" viewBox="0 0 20 20"><circle cx="10" cy="10" r="9" fill="none" stroke="#3176b5" stroke-width="1.5"/><polyline points="8,6 12,10 8,14" fill="none" stroke="#3176b5" stroke-width="1.5"/></svg>Quality Management</li>
    </ul>
  </div>
</section>

<section class="news">
  <h2>NEWS &amp; ARTICLES</h2>
  <div class="news-grid">
    <article class="news-card">
      <div class="news-img" role="img" aria-label="Delegation touring a production line" style="background:linear-gradient(135deg,#8fa3b8,#d9d3c8)"><span class="news-date">SEPTEMBER 2020</span></div>
      <p>Riverbend Industry Association visits Varlumo</p>
    </article>
    <article class="news-card">
      <div class="news-img" role="img" aria-label="Team hands joined together" style="background:linear-gradient(135deg,#c99a72,#efe3d6)"><span class="news-date">MAY 2019</span></div>
      <p>Varlumo joins an Innovation Electric Automation Alliance</p>
    </article>
    <article class="news-card">
      <div class="news-img" role="img" aria-label="Historic university building" style="background:linear-gradient(135deg,#9c5a44,#cfc2b2)"><span class="news-date">SEPTEMBER 2020</span></div>
      <p>Varlumo and academia join forces to drive innovation</p>
    </article>
  </div>
</section>

<footer class="footer">
  <div class="f-cols">
    <div class="f-col">
      <h4>Varlumo Electech Co., Ltd</h4>
      <p>12 Calder Road, Westfield Industrial Zone, Northgate City, Lindmoor Province</p>
      <p>Tel: (00) 0000-000000<br>Fax: (00) 0000-000000</p>
    </div>
    <div class="f-col">
      <h4>Hong Kong Office</h4>
      <p>8/F, Orrin Industrial Centre, 40 Orrin Street, Harbourside, Kowloon</p>
      <p>Tel: (000) 0000-0000<br>Fax: (000) 0000-0000</p>
    </div>
    <div class="f-col">
      <h4>Varlumo Schaltelemente GmbH Germany</h4>
      <p>Lindenweg 14, 00000 Feldhausen, Germany</p>
      <p>Email: info@varlumo-example.com<br>Tel: (00) 000 0000</p>
    </div>
    <div class="f-col">
      <h4>R&amp;D</h4>
      <p>5/F, 22 Calder Road, Valley Park, Northgate City, Lindmoor Province</p>
      <p>Email: rd@varlumo-example.com<br>Tel: (00) 0000-000000</p>
    </div>
  </div>
  <div class="f-bottom">
    <p>Copyright © 2020 Varlumo. All rights reserved. | Privacy Policy | Terms &amp; Conditions</p>
    <p style="margin-top:8px">About Us | Industries | Core Competencies | News | Locations &amp; Contacts</p>
    <div class="brand"><span class="mark"></span>Varlumo</div>
  </div>
</footer>

</body>
</html>
```